Affiliate website design and wireframe

We need a design of an affiliate website for an application we purchased, it is important that you build the website pages according to the developer of the applications specifications (please see attached documents) the developer of the application will configure the pages and add them to the site. Please take special note of his comments below.

We all so need you to create a wire frame so the developer can test everything (http://sketchwire.tolvaro.vn/)

It will be the homepage and about 16 inner pages (please see attached files)
Here is our website http://bluvendmarket.com/affiliate/affiliates/index.php

The version of the software we purchased is the Kivo Partner Hubline version

Comments from the developers

1. I will need the source files of the design (photoshop .psd files and font files if custom fonts are used), since the implementation is closely bound to component sizes (like border width, margin width etc.) and colors. If you own a corporate design manual, it's crucial to send it as well. Also, please, make sure if you use custom fonts, that these allow legal website integration (like google web fonts).

2. Any and every content is controlled via templates. All editing/adding/removing etc. is done here. The template files are essentially html/php documents, they use a template engine called quillo (http://www.quillo.net/) which has it's own language similar to php.

3. .psd files are ideal, because we deal with the specifics of KPX/KPH implementation on a daily basis. Any html/css developed in advance may prove to be a poor choice. You may choose to let an in-house developer do the job, but experience wise this is more costly, since he will not be accustomed to the template/functionality systems of KPX/KPH.

4. I will need the source files of the design (photoshop .psd files and font files if custom fonts are used), since the implementation is closely bound to component sizes (like border width, margin width etc.) and colors. If you own a corporate design manual, it's crucial to send it as well. Also, please, make sure if you use custom fonts, that these allow legal website integration (like google web fonts).

Regards,

Dorek Hanval
Multimedia Design

We prefer illustrations more than pictures of real people.

This is the home page, it is asking for Merchant and Affiliate sign up, not just affiliate.

http://bluvendmarket.com/affiliate/index.php

Please note the home page features both Merchant and Affiliate sign up

We are looking for illustration design not just stock images

Please remember the search menu that searches for the available programs, see the example we gave you, look at the search menu at the top of the page http://www.tradelumo.com/

We are reviewing everything, no need to send more designs

Target Market(s)

Natural Products Manufacturers
Natural products Sales reps
Natural Products Bloggers
Social Marketing

Industry/Entity Type

Software

Requirements
Must have
• 1. All links on pages should go to the appropriate pages.
2. Colors can be based on our logo design (look at the attachments)
3. Here is our website http://bluvendmarket.com/affiliate/affiliates/index.php
4. We have attached a drawing of how we think the homepage concept should follow.
5. Main concept of design, is trying to show our sales people (Affiliates) are doing multiple things to advertise and sell the merchants products.(see logo)
6. Need to be able to edit all text and images.
7. Our target audience is Natural product sales people (Advertisers, bloggers, ext) and natural product manufacturers.
8. You can speak to the company who made the application, through live chat, on there website http://www.kivopartnerhubline.com/
Nice to have
• See Attached Documents.
site should take up whole website pages
Look For fun Illustrated Website, one of the better ones we have seen is http://www.tradelumo.com/index.cfm
Should not have
• Please look very carefully at developers comment above.

```html
<!DOCTYPE html>
<html lang="en">
<head>
<meta charset="utf-8">
<title>BluvendMarket – Affiliate Home</title>
<link rel="stylesheet" href="https://fonts.googleapis.com/css2?family=Arimo:wght@400;700&family=Oswald:wght@700&display=swap">
<style>
:root{
  --navy:#0f3a68;
  --navy-dark:#12406b;
  --link-blue:#1f8fd6;
  --footer-head:#27a9e1;
  --footer-text:#b9c4cf;
  --panel:#d3dcd9;
  --band:#b6c6c0;
  --muted:#a3aeab;
  --green:#6cb33f;
  --ink:#111;
  --white:#fff;
}
*{box-sizing:border-box;margin:0;padding:0}
html,body{width:778px;height:1200px;overflow:hidden}
body{position:relative;font-family:"Arimo",Arial,sans-serif;background:var(--white);color:var(--ink)}
a{color:inherit;text-decoration:none}

.site-head{position:absolute;left:0;top:0;width:778px;height:400px;
  background:linear-gradient(#fff 0,#fff 30px,#c9d2cf 260px,#9eaca7 400px)}
.brand{position:absolute;left:17px;top:10px;width:182px;height:80px;background:#fff;
  display:flex;align-items:center;gap:8px;padding-left:4px}
.brand-mark{width:18px;height:18px;background:var(--navy);flex:none}
.brand-name{font-family:"Arimo",sans-serif;font-weight:700;font-size:15px;color:var(--green);letter-spacing:.2px}
.login-links{position:absolute;top:13px;right:16px;display:flex;gap:34px;font-size:11px;color:#3b4f7a}
.main-nav{position:absolute;top:70px;right:16px;display:flex;gap:30px;
  font-family:"Oswald",sans-serif;font-weight:700;font-size:16px;color:var(--navy-dark);letter-spacing:.3px}

.hero-frame{position:absolute;left:16px;top:100px;width:747px;height:284px;
  border:1px solid #9aa8a3;background:linear-gradient(#fff,#f2f5f4 70%,#c9d3cf)}
.hero{position:absolute;left:22px;top:23px;width:700px;height:237px;background:var(--navy)}
.signup-btn{position:absolute;top:173px;width:253px;height:49px;
  background:linear-gradient(#fff,#d6dddb 55%,#a7b4b0);
  display:flex;align-items:center;justify-content:center;
  font-weight:700;font-size:16px;color:var(--navy-dark)}
.signup-btn.affiliate{left:16px}
.signup-btn.merchant{left:431px}

.services{position:absolute;left:16px;top:428px;width:365px;height:479px;background:var(--panel)}
.services h2{position:absolute;left:25px;top:24px;font-size:24px;font-weight:700;color:var(--navy-dark)}
.service{position:absolute;left:0;width:365px;height:50px}
.service::after{content:"";position:absolute;left:0;top:25px;width:365px;height:24px;background:var(--band)}
.service-icon{position:absolute;left:24px;top:0;width:50px;height:50px;z-index:1;
  background:linear-gradient(#fff,#aab6b2);padding:3px}
.service-icon svg{display:block;width:44px;height:44px;background:var(--navy)}
.service-title{position:absolute;left:82px;top:12px;font-size:12px;font-weight:700;color:var(--muted);z-index:1}
.service-desc{position:absolute;left:82px;top:30px;font-size:12px;color:#2a3a55;z-index:1}

.intro{position:absolute;left:400px;top:428px;width:362px}
.intro h2{font-size:24px;font-weight:700}
.note p{font-size:12px;line-height:13.5px;margin-top:16px;color:#222}
.panels{position:absolute;left:402px;top:598px;width:360px}
.panels h2{font-size:24px;font-weight:700}
.panels a{display:block;font-size:12px;color:var(--link-blue);text-decoration:underline;margin-top:14px}
.panels a:first-of-type{margin-top:15px}
.samples{position:absolute;left:402px;top:758px;width:360px}
.samples h2{font-size:24px;font-weight:700;line-height:29px}
.samples p{font-size:12px;line-height:14px;margin-top:16px}

.site-foot{position:absolute;left:0;top:907px;width:778px;height:255px;background:var(--navy)}
.foot-col{position:absolute;top:32px;font-size:12px;color:var(--footer-text);line-height:14px}
.foot-col h3{font-size:15px;font-weight:400;color:var(--footer-head);margin-bottom:14px}
.foot-col a{display:block}
.foot-col.docs{left:20px;width:175px}
.foot-col.docs a{margin-bottom:14px}
.foot-col.about{left:206px;top:34px}
.foot-col.affiliates{left:387px;top:33px}
.foot-col.merchants{left:578px;top:33px}
.foot-col.about h3,.foot-col.affiliates h3,.foot-col.merchants h3{margin-bottom:13px}
.social{position:absolute;top:201px;left:574px;display:flex;gap:30px}
.social span{width:18px;height:18px;border-radius:50%;background:var(--footer-head)}
.copyright{position:absolute;left:0;top:1162px;width:778px;height:38px;background:#000;
  color:#fff;font-size:8px;font-weight:700;display:flex;align-items:center;justify-content:center}
</style>
</head>
<body>

<header class="site-head">
  <a class="brand" href="#"><span class="brand-mark"></span><span class="brand-name">BLUVENDMARKET</span></a>
  <nav class="login-links"><a href="#">AFFILIATES LOGIN</a><a href="#">MERCHANTS LOGIN</a></nav>
  <nav class="main-nav"><a href="#">HOME</a><a href="#">SIGNUP</a><a href="#">CONTACT US</a></nav>
  <div class="hero-frame">
    <div class="hero" role="img" aria-label="Hero illustration of affiliates promoting merchant products">
      <a class="signup-btn affiliate" href="#">AFFILIATES SIGNUP</a>
      <a class="signup-btn merchant" href="#">MERCHANT SIGNUP</a>
    </div>
  </div>
</header>

<section class="services">
  <h2>OUR SERVICES</h2>
  <div class="service" style="top:75px">
    <div class="service-icon"><svg viewBox="0 0 44 44"><ellipse cx="22" cy="19" rx="14" ry="11" fill="#1f4fd6"/><path d="M14 27 L12 36 L21 29Z" fill="#1f4fd6"/></svg></div>
    <div class="service-title">BLOG</div><div class="service-desc">Short one-line description</div>
  </div>
  <div class="service" style="top:125px">
    <div class="service-icon"><svg viewBox="0 0 44 44"><path d="M8 16 L30 8 L30 32 L8 24Z" fill="#1f4fd6"/><rect x="12" y="24" width="6" height="12" fill="#1f4fd6"/></svg></div>
    <div class="service-title">BANNER ADS</div><div class="service-desc">Short one-line description</div>
  </div>
  <div class="service" style="top:175px">
    <div class="service-icon"><svg viewBox="0 0 44 44"><rect x="8" y="12" width="28" height="20" fill="#1f4fd6"/><path d="M8 12 L22 24 L36 12" fill="none" stroke="#0f3a68" stroke-width="2"/></svg></div>
    <div class="service-title">E-MAILS</div><div class="service-desc">Short one-line description</div>
  </div>
  <div class="service" style="top:225px">
    <div class="service-icon"><svg viewBox="0 0 44 44"><rect x="8" y="9" width="28" height="20" rx="4" fill="#1f4fd6"/><path d="M16 29 L14 37 L24 29Z" fill="#1f4fd6"/></svg></div>
    <div class="service-title">TEXT MESSAGES</div><div class="service-desc">Short one-line description</div>
  </div>
  <div class="service" style="top:275px">
    <div class="service-icon"><svg viewBox="0 0 44 44"><path d="M13 8 L19 8 L21 16 L17 19 Q20 26 26 29 L29 25 L37 27 L37 33 Q30 38 20 30 Q10 21 13 8Z" fill="#1f4fd6"/></svg></div>
    <div class="service-title">PHONE CALLS</div><div class="service-desc">Short one-line description</div>
  </div>
  <div class="service" style="top:325px">
    <div class="service-icon"><svg viewBox="0 0 44 44" role="img" aria-label="Social networking icon"><rect x="10" y="14" width="24" height="20" fill="#1f4fd6"/></svg></div>
    <div class="service-title">SOCIAL NETWORKING</div><div class="service-desc">Short one-line description</div>
  </div>
</section>

<section class="intro note">
  <h2>Note!</h2>
  <p>This page (index.php in template root_index.stpl) is the initial page only to give you the most used links, and to walk you through various possibilities of the affiliate system.</p>
  <p style="margin-top:14px">When you are ready to go online with your affiliate program, you can freely delete or change this page (template root_index.stpl).</p>
</section>

<section class="panels">
  <h2>Panels</h2>
  <a href="#">Merchant (admin) panel</a>
  <a href="#">Affiliate panel</a>
  <a href="#">Affiliate mini site (with signup form)</a>
</section>

<section class="samples">
  <h2>Samples &amp; tests page - recommended</h2>
  <p>Samples &amp; tests pages<br>here are examples of use and demonstrations of banners, clicks and sales tracking, custom signup form, etc..</p>
</section>

<footer class="site-foot">
  <div class="foot-col docs"><h3>Documentation</h3>
    <a href="#">Introduction Videos</a><a href="#">Documentation &amp; support</a><a href="#">New plugins, themes and other extras library</a></div>
  <div class="foot-col about"><h3>About us</h3>
    <a href="#">Company</a><a href="#">Contact us</a><a href="#">Privacy Policy</a></div>
  <div class="foot-col affiliates"><h3>Affiliates</h3>
    <a href="#">Affiliates information</a><a href="#">Affiliate link formats</a></div>
  <div class="foot-col merchants"><h3>Merchants</h3>
    <a href="#">Merchants Login</a><a href="#">&nbsp;Integration methods</a><a href="#">API Reference</a><a href="#">Samples and Tests</a><a href="#">Kivo Partner Pro</a></div>
  <div class="social"><span></span><span></span><span></span></div>
</footer>
<div class="copyright">Copyright : etc.</div>

</body>
</html>
```